Quillmark Solutions - Website for a CRM IT Services Provider to Non-profits

We need a website design for our company that provides IT services to non-profits to enable them to manage their donors and philanthropy within their organization.

We would like to see a design that uses the colors in our logo and a funky take on how to uniquely present a topic as boring as IT. Examples of sites that we really like: brantwickdale.com, www.marlowpetrie.com, tinwhistlebox.com

The final design should communicate that we are a professional, yet creative company that is fun to work with.

Target Market(s)

Non-profits who tend to be young, creative types that are low-tech

Industry/Entity Type

It Company

Requirements
Must have
• Must include tabs for Home, Contact Us, About, Projects, and Blog. The site must use the logo we have attached on all of the page, in one way or another (it can be small & in the corner).

The site has to work on all mobile browsers (iphone, ipad).
Nice to have
• It would be great if I could supply some HTML for the Contact page that would allow me to capture leads and put them directly into my CRM application. It's very easy to set up.
Should not have
• The design should not use old-style fonts and should not have a lot of dark colors. Keep it similar to our logo, clean and simple. We're not looking for a busy home page.

```html
<!DOCTYPE html>
<html lang="en">
<head>
<meta charset="utf-8">
<title>Quillmark Solutions – Contact Us</title>
<link rel="stylesheet" href="https://fonts.googleapis.com/css2?family=Quicksand:wght@700&family=Kalam:wght@700&display=swap">
<style>
  :root {
    --sea: #3b9bb2;
    --sea-deep: #2c7f95;
    --glow: #72eeea;
    --ink: #0d5568;
    --nav-ink: #0f4b5c;
    --field-line: #1b98ad;
    --card: #ffffff;
    --button-top: #3a8a9c;
    --button-bottom: #14586a;
    --foam: #bfe6ec;
  }
  * { box-sizing: border-box; margin: 0; padding: 0; }
  html, body { width: 1200px; height: 1015px; overflow: hidden; }
  body {
    position: relative;
    background:
      radial-gradient(ellipse 330px 230px at 610px 0, rgba(114,238,234,0.95), rgba(114,238,234,0.35) 55%, rgba(114,238,234,0) 100%),
      var(--sea);
    font-family: Arial, Helvetica, sans-serif;
  }
  .brand { position: absolute; left: 210px; top: 24px; width: 100px; text-align: center; }
  .brand-mark {
    width: 84px; height: 84px; margin: 0 auto; border-radius: 50%;
    background: radial-gradient(circle at 40% 35%, #f2fbf9, #b9e8e2);
  }
  .brand-name {
    margin-top: 6px; color: #ffffff; font-family: Quicksand, sans-serif;
    font-weight: 700; font-size: 13px; line-height: 1.1;
  }
  .main-nav { position: absolute; top: 54px; left: 0; width: 1200px; height: 37px; }
  .main-nav a {
    position: absolute; top: 0; height: 37px; line-height: 37px;
    font-family: Quicksand, sans-serif; font-weight: 700; font-size: 14px;
    letter-spacing: 1.2px; color: var(--nav-ink); text-decoration: none;
    white-space: nowrap;
  }
  .main-nav a.is-active {
    background: linear-gradient(#2f8ea3, #17627a); color: #ffffff;
    width: 115px; text-align: center; letter-spacing: 1px;
  }
  .contact-card {
    position: absolute; left: 278px; top: 205px; width: 624px; height: 428px;
    background: var(--card); border-radius: 11px;
    box-shadow: 0 0 0 1px #2a92a8;
  }
  .field-label {
    position: absolute; left: 61px; font-size: 14.5px; line-height: 17px; color: var(--ink);
    white-space: nowrap;
  }
  .field-input {
    position: absolute; left: 192px; width: 305px; height: 22px;
    border: 1px solid var(--field-line); border-radius: 3px; background: #fff;
  }
  .submit-button {
    position: absolute; left: 251px; top: 363px; width: 122px; height: 32px;
    border: 1px solid #0f4a59; border-radius: 2px;
    background: linear-gradient(var(--button-top), var(--button-bottom));
    color: #ffffff; font-size: 14.5px; font-family: Arial, Helvetica, sans-serif;
  }
  .reef-art {
    position: absolute; left: 210px; top: 640px; width: 750px; height: 175px;
    background: radial-gradient(ellipse 50% 60% at 50% 60%, rgba(150,210,222,0.35), rgba(150,210,222,0));
  }
  .sea-floor { position: absolute; left: 0; top: 770px; }
  .footer-mark {
    position: absolute; left: 235px; top: 812px; width: 52px; height: 52px;
    border-radius: 50%; background: rgba(150,205,215,0.55);
  }
  .copyright {
    position: absolute; left: 233px; top: 870px;
    font-size: 9px; color: var(--foam); white-space: nowrap;
  }
  .connect-title {
    position: absolute; left: 846px; top: 825px; font-family: Kalam, cursive;
    font-size: 11px; color: #ffffff; letter-spacing: 0.5px; white-space: nowrap;
  }
  .social-link {
    position: absolute; top: 849px; width: 30px; height: 30px; border-radius: 50%;
  }
  .social-link.first { left: 858px; background: #6a84c0; }
  .social-link.second { left: 896px; background: #4fc4ea; }
</style>
</head>
<body>
  <header>
    <div class="brand">
      <div class="brand-mark"></div>
      <div class="brand-name">Quillmark Solutions</div>
    </div>
    <nav class="main-nav">
      <a href="#" style="left:440px">HOME</a>
      <a href="#" class="is-active" style="left:515px">CONTACT US</a>
      <a href="#" style="left:660px">ABOUT</a>
      <a href="#" style="left:750px">PROJECTS</a>
      <a href="#" style="left:866px">BLOG</a>
    </nav>
  </header>

  <form class="contact-card">
    <label class="field-label" style="top:59px">FIRST NAME</label>
    <span class="field-input" style="top:56px"></span>
    <label class="field-label" style="top:101px">LAST NAME</label>
    <span class="field-input" style="top:97px"></span>
    <label class="field-label" style="top:147px">EMAIL</label>
    <span class="field-input" style="top:143px"></span>
    <label class="field-label" style="top:195px">COMPANY</label>
    <span class="field-input" style="top:190px"></span>
    <label class="field-label" style="top:248px">CITY</label>
    <span class="field-input" style="top:241px"></span>
    <label class="field-label" style="top:294px">STATE</label>
    <span class="field-input" style="top:293px"></span>
    <button type="button" class="submit-button">SUBMIT</button>
  </form>

  <div class="reef-art" role="img" aria-label="Faint seaweed and bubbles illustration"></div>

  <svg class="sea-floor" width="1200" height="245" viewBox="0 0 1200 245" aria-hidden="true">
    <path fill="var(--sea-deep)" d="M0 40 Q30 12 60 32 Q100 10 140 28 Q190 0 240 26 Q290 4 330 30 Q370 10 410 32 Q460 8 520 30 Q560 0 620 22 Q680 -4 730 28 Q770 12 800 30 Q840 10 880 34 Q920 14 950 30 Q1010 -6 1090 20 Q1140 0 1165 32 Q1185 8 1200 14 L1200 245 L0 245 Z"/>
  </svg>

  <footer>
    <div class="footer-mark"></div>
    <p class="copyright">copyright 2012</p>
    <p class="connect-title">CONNECT WITH US</p>
    <a href="#" class="social-link first" aria-label="Social profile"></a>
    <a href="#" class="social-link second" aria-label="Social profile"></a>
  </footer>
</body>
</html>
```